New, modern business card for growing audiology practice

We need a new business card for our audiology practice. Our logo and website have recently changed (more modern) and we want our business cards to reflect this change.
We conduct hearing tests, perform earwax removals, and fit & dispense hearing aids to our patients. We are a family owned practice in which the owner is the one who works directly with the patient. I have attached logos in various formats to use, as well as two ideas I found on this website; as well as a scanned copy of our current logo. Good luck!

Industry/Entity Type

Business

Contact Information for Business Card

Company name: Maplow Hearing Center
Provider name: Peter Mulvoy, Au.D. F/ISN
Phone number: (555) 318-6042
Address: 87 W. Linden Ave. Larkfield, OH 45190
email: maplowhearing@postvale.net
website: maplowhearing.com

Colors
000000
aaaaaa
dbdbdb
cacaca
9bcb3c
afd23c
cadf82
b1b1b1

Requirements
Must have
• My card must include information in the "details" section. In the attached images, I found a few that I liked and I would like to model after - "brisk tumblin'" and "Sound Wellness Center".
• Must be horizontal.
• Must include logos provided. I uploaded them in various file formats and various ways.
• Must match logo font, if possible, if not, please get as close as you can.
Nice to have
• I really like the idea of having a color on one side with just the logo and company name and the contact information and provider name on the other side. I also really like the idea of having the main color dominating on the logo/company side with accent of that same color on the contact side of the card.
Should not have
• Must not be vertical.

```html
<!DOCTYPE html>
<html lang="en">
<head>
<meta charset="utf-8">
<title>Maplow Hearing Center – Business Card</title>
<link rel="stylesheet" href="https://fonts.googleapis.com/css2?family=Questrial&family=Montserrat:wght@400;600;700&display=swap">
<style>
  :root {
    --backdrop: #e4e4e6;
    --card-white: #ffffff;
    --brand-green: #9bcb3c;
    --accent-green: #afd23c;
    --pattern-grey: #b1b1b1;
    --ink: #000000;
    --ink-soft: #333333;
    --shadow: rgba(0, 0, 0, 0.18);
  }
  * { margin: 0; padding: 0; box-sizing: border-box; }
  html, body { width: 1200px; height: 796px; overflow: hidden; }
  body { background: var(--backdrop); position: relative; font-family: "Questrial", sans-serif; }

  .card {
    position: absolute;
    width: 560px;
    height: 320px;
    box-shadow: 0 6px 18px var(--shadow);
    overflow: hidden;
  }

  /* Contact side */
  .card--contact { left: 580px; top: 50px; background: var(--card-white); }
  .brand {
    position: absolute; left: 34px; top: 38px;
    display: flex; align-items: center; gap: 12px;
    white-space: nowrap;
  }
  .brand__dot { flex: none; width: 30px; height: 30px; border-radius: 50%; background: var(--brand-green); }
  .brand__name {
    font-family: "Questrial", sans-serif;
    font-size: 31px; letter-spacing: -0.5px;
    text-transform: uppercase; color: var(--ink);
  }
  .provider {
    position: absolute; left: 0; right: 0; top: 118px;
    padding-left: 60px;
    text-align: center; line-height: 1.35;
  }
  .provider__name {
    font-family: "Montserrat", sans-serif; font-weight: 700;
    font-size: 19px; letter-spacing: 4px; text-transform: uppercase;
    color: var(--brand-green);
  }
  .provider__credentials { font-family: "Montserrat", sans-serif; font-size: 13px; color: var(--ink-soft); }
  .provider__title { font-family: "Montserrat", sans-serif; font-size: 14px; letter-spacing: 1.5px; color: var(--ink-soft); }
  .provider__phone {
    font-family: "Montserrat", sans-serif; font-weight: 700;
    font-size: 19px; letter-spacing: 3px; color: var(--brand-green);
  }
  .address {
    position: absolute; left: 34px; bottom: 30px;
    font-family: "Montserrat", sans-serif; font-size: 14px;
    letter-spacing: 2px; color: var(--ink-soft);
    white-space: nowrap;
  }

  /* Brand side */
  .card--brand { left: 80px; top: 420px; background: var(--brand-green); }
  .card__pattern { position: absolute; inset: 0; background: var(--brand-green); }
  .website {
    position: absolute; left: 120px; bottom: 42px;
    font-family: "Montserrat", sans-serif; font-weight: 600;
    font-size: 17px; letter-spacing: 2.5px; color: var(--ink-soft);
  }
  .brand--mini { left: auto; top: auto; right: 34px; bottom: 96px; gap: 8px; }
  .brand--mini .brand__dot { width: 18px; height: 18px; background: var(--ink); }
  .brand--mini .brand__name { font-size: 15px; }
</style>
</head>
<body>

  <section class="card card--contact">
    <div class="brand">
      <span class="brand__dot"></span>
      <span class="brand__name">Maplow Hearing Center</span>
    </div>
    <div class="provider">
      <p class="provider__name">Peter Mulvoy</p>
      <p class="provider__credentials">Au.D. F/ISN</p>
      <p class="provider__title">Owner – Audiologist</p>
      <p class="provider__phone">(555) 318-6042</p>
    </div>
    <p class="address">87 W. Linden Ave. Larkfield, OH 45190</p>
  </section>

  <section class="card card--brand">
    <div class="card__pattern" role="img" aria-label="Repeating grey curved pattern on lime green background"></div>
    <div class="brand brand--mini">
      <span class="brand__dot"></span>
      <span class="brand__name">Maplow Hearing Center</span>
    </div>
    <p class="website">MaplowHearing.com</p>
  </section>

</body>
</html>
```